Ledgerwise Reach - B2B Demand Generation Website Project

We need a fully functional website for www.ledgerwisereach.example. We are a B2B Demand Generation company, based in London, working with companies such as QRT, VKD, Norvex, Brindlow, Tarvo generating them sales leads for their sales teams. We run this through digital marketing newsletter promotions and have a network of websites. Content syndication, data, demand generation, online marketing. Our logo has just been redone (attached) and we have a holding page already which i would like to use the style / colours. Our logo is bright and vibrant but i dont want the site to be a rainbow. We are expensive, classy, professorial, B2B, intelligent.

Home
About Us
Our Services
Prospora & QA Technology
Intent Data
Testimonials
Contact Us
Updates

Target Market(s)

B2B Marketers (QRT, Velquarion, Tarvo, VKD, Opal Reach, Driftmoor, Harlow Quantis, Technology Companies, Data Companies, Marketing Teams, Tumbleden.

Industry/Entity Type

Marketing

Coding

Coded - Design and coding required

Number of Pages Required

5+ page

Font styles to use
Sans Serif

Requirements
Must have
• Home
About Us
Our Services
Prospora & QA Technology
Intent Data
Testimonials
Contact Us

Simple Pages.

Look classy, intelligent, data experts. I like the video homepages were the image moves at the top. Very soft animation.
Nice to have
• Websites i like:

https://www.vkd.example/
https://www.brevantor.example/
https://www.plumfieldsites.example.co.uk/

Ledgerwise Reach - The Demand Generation Company
Should not have
• Glimpsevault crap images

```html
<!DOCTYPE html>
<html lang="en">
<head>
<meta charset="utf-8">
<title>Ledgerwise Reach – Home page, blue and red themes</title>
<link href="https://fonts.googleapis.com/css2?family=Montserrat:wght@500;600;700;800&family=Poppins:wght@400;500;600&display=swap" rel="stylesheet">
<style>
:root{
  --page:#ffffff;
  --mist:#eef1f7;
  --ink:#1d2233;
  --muted:#8a90a2;
  --line:#e6e9f2;
  --tick:#2aa84a;
  --footer:#1c1c1f;
  --base:#0b0b0c;
  --blue:#1c3fd6;
  --blue-deep:#0f2596;
  --red:#e8263c;
  --red-deep:#b3101f;
}
*{margin:0;padding:0;box-sizing:border-box}
html,body{width:676px;height:1200px;overflow:hidden;background:var(--page)}
body{font-family:"Poppins",Arial,sans-serif;color:var(--ink)}
.stage{position:absolute;left:0;top:0;width:1450px;height:2574px;transform:scale(.46621);transform-origin:0 0}
.site{position:absolute;top:0;width:408px;height:2576px;background:var(--page);overflow:hidden}
.theme-blue{--a1:var(--blue);--a1d:var(--blue-deep);--a2:var(--red);--hero:#0b1240;--hero2:#1a2aa0;--soft:#aeb9ee;--intent1:#3a0608;--intent2:#8b0a10}
.theme-red{--a1:var(--red);--a1d:var(--red-deep);--a2:var(--blue);--hero:#130b0d;--hero2:#2a1216;--soft:#f3aab3;--intent1:#3a0608;--intent2:#8b0a10}
.abs{position:absolute}
.sec{position:absolute;left:0;width:408px}
.photo{position:absolute}

/* hero */
.hero{top:0;height:198px;background:linear-gradient(100deg,var(--hero) 0%,var(--hero) 45%,var(--hero2) 100%)}
.brand{display:flex;align-items:center;gap:4px;color:#fff;font-family:"Montserrat",sans-serif;font-weight:600;font-size:8px}
.brand i{width:11px;height:11px;border-radius:50%;border:1.5px solid #fff;display:block}
.brand small{display:block;font-size:2.4px;font-weight:500;opacity:.7;font-family:"Poppins",sans-serif}
.nav{display:flex;gap:5px;color:#fff;font-size:3.2px;font-weight:600;text-transform:uppercase}
.hero h1{font-family:"Montserrat",sans-serif;font-weight:800;color:#fff;font-size:14.5px;line-height:22px}
.hero p{color:#d4d8ea;font-size:3.8px;line-height:6.5px;width:150px}
.play{width:13px;height:13px;border-radius:50%;border:1px solid #fff;display:flex;align-items:center;justify-content:center}
.pill{border-radius:7px;color:#fff;font-size:3px;font-weight:600;display:flex;align-items:center;justify-content:center;gap:3px}
.phone-box{left:255px;top:164px;width:153px;height:34px;background:var(--a1);color:#fff}
.phone-box b{font-size:5px;font-weight:600}
.phone-box span{font-size:2.8px;opacity:.8}
.clients{top:198px;height:67px;width:255px;background:var(--mist)}
.client{position:absolute;top:28px;font-family:"Poppins",sans-serif;font-weight:600;font-size:6px;color:#5a6070;display:flex;align-items:center;gap:2px}
.client i{width:4px;height:4px;background:#5a6070;display:block;border-radius:50%}
.who{left:255px;top:198px;width:153px;height:34px;background:var(--a1);color:#fff;font-family:"Montserrat",sans-serif;font-weight:700;font-size:6px;display:flex;align-items:center;justify-content:center;letter-spacing:.2px}
.consult-tab{left:255px;top:232px;width:153px;height:33px;background:var(--a1d);color:#fff}
.consult-tab b{font-size:4.4px;font-weight:600}
.consult-tab span{font-size:2.7px;opacity:.8;line-height:4px}
.arrow{color:#fff;font-size:6px;line-height:1}

/* headings */
.eyebrow{font-family:"Montserrat",sans-serif;font-weight:800;font-size:6px;letter-spacing:1px;color:var(--a1);text-transform:uppercase}
.outline{font-family:"Montserrat",sans-serif;font-weight:700;font-size:14px;line-height:22px;color:transparent;-webkit-text-stroke:.55px var(--soft)}
.center{left:0;width:408px;text-align:center}
.on-dark .outline{-webkit-text-stroke:.55px #ffffffb0}

/* about */
.body-copy{font-size:3.6px;line-height:6px;color:#6b7183}
.body-copy p{margin-bottom:5.5px}
.ticks li{list-style:none;display:flex;align-items:center;gap:4px;color:var(--tick);font-size:3.4px;font-weight:500;height:13px}
.ticks svg{width:7px;height:7px;flex:none}

/* stats */
.stat{position:absolute;background:#fff;box-shadow:0 2px 10px #1d223314;text-align:center}
.stat span{display:block;font-size:4px;font-weight:600;margin-top:17px}
.stat b{display:block;font-family:"Montserrat",sans-serif;font-weight:700;font-size:10px;margin-top:3px}
.stat.lead{background:linear-gradient(120deg,var(--a1),var(--a1d));color:#fff;box-shadow:none}
.stat.lead span{margin-top:16px}

/* timeline */
.rail{left:203.5px;width:1px}
.node{position:absolute;width:5px;height:5px;border-radius:50%}
.hub{position:absolute;width:58px;height:58px;border-radius:50%;border:3px solid #fff;box-shadow:0 0 0 1px var(--line),0 4px 12px #1d22331f;color:#fff;font-size:3.6px;font-weight:600;display:flex;align-items:center;justify-content:center}
.feat{position:absolute;width:120px;height:67px;background:#fff;border:1px solid #edf0f6;padding:13px 9px}
.feat h4{font-size:4.6px;font-weight:600;margin-bottom:4px}
.feat p{font-size:3px;line-height:5px;color:#8a90a2;width:95px}
.feat .glyph{position:absolute;right:9px;top:9px;width:22px;height:22px;border:1px solid #e4e7ef;border-radius:50%}
.grp1 h4{color:var(--a1)}
.grp2 h4{color:var(--a2)}
.feat.on1{border-color:var(--a1);box-shadow:0 3px 10px #1d223318}
.feat.on2{border-color:var(--a2);box-shadow:0 3px 10px #1d223318}

/* services */
.services{background:var(--mist)}
.svc-card{position:absolute;top:70px;width:105px;height:107px}
.svc-card.main{background:linear-gradient(150deg,var(--a1),var(--a1d));color:#fff;padding:12px 9px}
.svc-card.main hr{width:8px;border:0;border-top:1px solid #fff;margin-bottom:4px}
.svc-card.main h4{font-size:3.8px;font-weight:600;margin-bottom:5px}
.svc-card.main p{font-size:3px;line-height:5px;opacity:.9}

/* QA */
.qa{background:linear-gradient(120deg,#0a1470 0%,#0e1f9e 55%,#1632c0 100%)}
.qa .eyebrow{color:#fff}
.qa-item{position:absolute;left:35px;display:flex;gap:6px;align-items:flex-start}
.qa-item i{width:12px;height:12px;border-radius:50%;background:#fff;display:block;flex:none}
.qa-item b{display:block;color:#fff;font-size:3.8px;font-weight:600;margin-top:1px}
.qa-item span{color:#c9d0f2;font-size:3px}

/* consultancy */
.consult{background:var(--a1);color:#fff;text-align:center}
.consult h3{font-family:"Montserrat",sans-serif;font-size:7px;font-weight:700}
.consult p{font-size:3.3px;opacity:.85}
.field{position:absolute;top:48px;width:76px;height:12px;background:#ffffff22;color:#fff;font-size:3px;text-align:left;padding:4px 6px}
.consult .pill{position:absolute;top:48px;left:292px;width:50px;height:12px;border:1px solid #ffffffaa}

/* testimonials */
.testi{background:var(--mist)}
.quote-card{position:absolute;left:62px;width:287px;height:113px;background:#fff;box-shadow:0 4px 18px #1d223312}
.stack{position:absolute;background:#fff;opacity:.6}
.avatar{position:absolute;left:20px;top:26px;width:40px;height:40px;border-radius:50%;background:linear-gradient(160deg,#6e6a68,#2d2b2c)}
.who-name{position:absolute;left:0;width:80px;text-align:center;font-size:3.6px;font-weight:600}
.who-co{position:absolute;left:0;width:80px;text-align:center;font-size:2.8px;color:var(--muted)}
.quote{position:absolute;left:73px;top:26px;width:190px;font-size:3.6px;line-height:6px;color:#6b7183}
.round{position:absolute;width:24px;height:24px;border-radius:50%;background:var(--a1);color:#fff;display:flex;align-items:center;justify-content:center;font-size:8px;box-shadow:0 3px 8px #1d223330}
.more{position:absolute;left:180px;width:48px;height:10px;border:1px solid var(--a1);border-radius:6px;color:var(--a1);font-size:2.8px;display:flex;align-items:center;justify-content:center;gap:2px}

/* intent */
.intent{background:linear-gradient(90deg,var(--intent2) 0%,var(--intent1) 55%,#2a0406 100%)}
.intent .eyebrow{color:#fff}
.intent p{font-size:3.3px;line-height:5.5px;color:#f1d6d8;text-align:right}

/* blog */
.blog{background:var(--mist)}
.post{position:absolute;top:70px;width:95px;height:143px;background:#fff;box-shadow:0 3px 12px #1d223312}
.post .photo{left:0;top:0;width:95px;height:66px}
.post h4{position:absolute;left:9px;top:75px;font-size:4px;font-weight:600;color:var(--a1)}
.post p{position:absolute;left:9px;top:86px;width:77px;font-size:3px;line-height:5px;color:#8a90a2}
.post .meta{position:absolute;left:9px;top:128px;width:77px;display:flex;justify-content:space-between;font-size:2.8px;color:#8a90a2}
.side-arrow{position:absolute;color:var(--a1);font-size:7px}

/* footer */
.footer{top:2330px;height:125px;background:var(--footer);color:#fff}
.fcol{position:absolute;top:36px}
.fcol h5{font-size:4.4px;font-weight:500;margin-bottom:6px}
.fcol li{list-style:none;font-size:3px;color:#a3a7b3;line-height:8.4px}
.news-field{position:absolute;left:278px;top:71px;width:112px;height:16px;border:1px solid #ffffffcc;border-radius:8px;font-size:3.3px;padding:5px 8px;color:#fff}
.base{top:2455px;height:121px;background:var(--base);color:#fff}
.base p{font-size:3.2px;line-height:5px;color:#a3a7b3}
.reach-box{position:absolute;left:142px;width:104px;color:#fff;padding:10px 8px}
.reach-box span{display:block;font-size:3px;line-height:4.6px;opacity:.9}
.reach-box b{display:block;font-size:4px;font-weight:600;margin-top:6px}
.dot{display:inline-block;width:4px;height:4px;border-radius:50%;background:#fff;margin-left:6px;vertical-align:middle}
</style>
</head>
<body>
<div class="stage">

<!-- ============ Blue theme ============ -->
<div class="site theme-blue" style="left:298px">

  <section class="sec hero">
    <div class="photo" role="img" aria-label="Portrait of a businessman in a suit adjusting his tie" style="left:225px;top:0;width:183px;height:198px;background:linear-gradient(180deg,#14205e 0%,#2c3aa0 50%,#101846 100%)"></div>
    <div class="abs brand" style="left:38px;top:10px"><i></i><div>ledgerwisereach<small>The Demand Generation Company</small></div></div>
    <nav class="abs nav" style="left:162px;top:15px"><span>Home</span><span>About</span><span>Services</span><span>Prospora &amp; QA Technology</span><span>Intent Data</span><span>Testimonials</span><span>Contact</span></nav>
    <h1 class="abs" style="left:40px;top:62px">Grow Your Business With<br>Ledgerwise Reach</h1>
    <p class="abs" style="left:40px;top:110px">Check out our marketing, sales and services to that helps your business grow. Getting good service will ensure that your customers receive good service.</p>
    <div class="abs play" style="left:41px;top:141px"><svg width="4" height="5" viewBox="0 0 4 5"><path d="M0 0L4 2.5L0 5Z" fill="#fff"/></svg></div>
    <div class="abs pill" style="left:62px;top:141px;width:47px;height:12px;background:var(--a1)">GET STARTED <span>→</span></div>
  </section>

  <div class="abs phone-box" style="padding:9px 15px">
    <b>&#9990; +44 20 7946 0321</b><br><span>Monday - Friday 9:00AM - 6:00PM</span>
    <span class="abs arrow" style="left:112px;top:11px">‹</span><span class="abs arrow" style="left:139px;top:11px">›</span>
  </div>
  <div class="sec clients">
    <div class="client" style="left:10px"><i></i>Brindlow</div>
    <div class="client" style="left:64px">Norvex</div>
    <div class="client" style="left:112px">QRT</div>
    <div class="client" style="left:160px">Tarvo</div>
    <div class="client" style="left:208px">VKD</div>
  </div>
  <div class="abs who">WHO WE WORK WITH</div>
  <div class="abs consult-tab">
    <span class="abs arrow" style="left:11px;top:11px">‹</span><span class="abs arrow" style="left:38px;top:11px">›</span>
    <div class="abs" style="left:70px;top:7px;width:78px"><b>&#9993; Free Consultation</b><span>Request a free assessment and get started today.</span></div>
  </div>

  <div class="abs eyebrow center" style="top:284px">About Us</div>
  <h2 class="abs outline center" style="top:300px">Marketing and Advertising Solutions<br>for Your Business</h2>
  <div class="abs body-copy" style="left:39px;top:357px;width:160px">
    <p>Ledgerwise Reach can deliver high quality sales leads from any country in the world. This can include leads via email or telemarketing, account-based targeting (ABM) or identifying need and pain points through BANT / SQL campaigns.</p>
    <p>Ledgerwise Reach offer expert demand generation support, from providing detailed leads of qualified decision makers, to a comprehensive lead generation and SQL service.</p>
    <p>Our extensive and ongoing research campaigns give you the ability to build contact lists that identify individuals at all stages of the buying cycle, from pre-sales to sales ready.</p>
    <p>With access to over 31 million names, Ledgerwise Reach offers a range of marketing options that allow you to use our data to target the decision makers you need to reach.</p>
    <p>This can include:</p>
    <ul class="ticks">
      <li><svg viewBox="0 0 8 8"><circle cx="4" cy="4" r="4" fill="var(--tick)"/><path d="M2.2 4.1L3.5 5.3L5.9 2.8" stroke="#fff" stroke-width=".9" fill="none"/></svg>Breakdown by geography, job title, role and responsibility</li>
      <li><svg viewBox="0 0 8 8"><circle cx="4" cy="4" r="4" fill="var(--tick)"/><path d="M2.2 4.1L3.5 5.3L5.9 2.8" stroke="#fff" stroke-width=".9" fill="none"/></svg>Targeting through previous research and buying intention</li>
      <li><svg viewBox="0 0 8 8"><circle cx="4" cy="4" r="4" fill="var(--tick)"/><path d="M2.2 4.1L3.5 5.3L5.9 2.8" stroke="#fff" stroke-width=".9" fill="none"/></svg>Email dispatch to selected individuals</li>
      <li><svg viewBox="0 0 8 8"><circle cx="4" cy="4" r="4" fill="var(--tick)"/><path d="M2.2 4.1L3.5 5.3L5.9 2.8" stroke="#fff" stroke-width=".9" fill="none"/></svg>Extensive telemarketing options</li>
    </ul>
  </div>
  <div class="photo" role="img" aria-label="Glass office towers seen from below against a blue sky" style="left:208px;top:357px;width:161px;height:185px;background:linear-gradient(160deg,#dfe9f3 0%,#8fb0cc 40%,#3b6b93 100%)"></div>
  <div class="photo" role="img" aria-label="Team meeting in a bright glass-walled office" style="left:201px;top:447px;width:78px;height:102px;border:4px solid #fff;background:linear-gradient(170deg,#c9d3da,#6f7f8a)"></div>

  <div class="stat lead" style="left:149px;top:587px;width:109px;height:52px"><span>Leads Delivered Per Month</span><b>25.000+</b></div>
  <div class="stat" style="left:39px;top:640px;width:109px;height:53px"><span>Downloads Per Month</span><b>70.000+</b></div>
  <div class="stat" style="left:259px;top:640px;width:109px;height:53px"><span>Countries We Can Reach</span><b>50+</b></div>

  <div class="abs rail" style="top:680px;height:497px;background:linear-gradient(180deg,var(--a1) 0%,var(--a1) 52%,var(--a2) 52%,var(--a2) 100%);opacity:.5"></div>
  <div class="node" style="left:201.5px;top:678px;background:var(--a1)"></div>
  <div class="node" style="left:201.5px;top:1175px;background:var(--a2)"></div>

  <div class="feat grp1 on1" style="left:71px;top:727px"><h4>Service</h4><p>Lorem ipsum dolor sit amet, consectetur adipiscing elit, sed do eiusmod tempor incididunt ut labore et dolore magna aliqua.</p><i class="glyph"></i></div>
  <div class="feat grp1" style="left:217px;top:727px"><h4>Improvement</h4><p>Lorem ipsum dolor sit amet, consectetur adipiscing elit, sed do eiusmod tempor incididunt ut labore et dolore magna aliqua.</p><i class="glyph"></i></div>
  <div class="feat grp1" style="left:39px;top:812px"><h4>Satisfaction</h4><p>Lorem ipsum dolor sit amet, consectetur adipiscing elit, sed do eiusmod tempor incididunt ut labore et dolore magna aliqua.</p><i class="glyph"></i></div>
  <div class="feat grp1" style="left:248px;top:812px"><h4>Business</h4><p>Lorem ipsum dolor sit amet, consectetur adipiscing elit, sed do eiusmod tempor incididunt ut labore et dolore magna aliqua.</p><i class="glyph"></i></div>
  <div class="feat grp1" style="left:71px;top:896px"><h4>Standard</h4><p>Lorem ipsum dolor sit amet, consectetur adipiscing elit, sed do eiusmod tempor incididunt ut labore et dolore magna aliqua.</p><i class="glyph"></i></div>
  <div class="feat grp1" style="left:217px;top:896px"><h4>Customer</h4><p>Lorem ipsum dolor sit amet, consectetur adipiscing elit, sed do eiusmod tempor incididunt ut labore et dolore magna aliqua.</p><i class="glyph"></i></div>
  <div class="hub" style="left:175px;top:816px;background:var(--a1)">QA Technology</div>

  <div class="feat grp2 on2" style="left:39px;top:1015px"><h4>Generate</h4><p>Lorem ipsum dolor sit amet, consectetur adipiscing elit, sed do eiusmod tempor incididunt ut labore et dolore magna aliqua.</p><i class="glyph"></i></div>
  <div class="feat grp2" style="left:248px;top:1015px"><h4>Capture</h4><p>Lorem ipsum dolor sit amet, consectetur adipiscing elit, sed do eiusmod tempor incididunt ut labore et dolore magna aliqua.</p><i class="glyph"></i></div>
  <div class="feat grp2" style="left:71px;top:1099px"><h4>Qualify</h4><p>Lorem ipsum dolor sit amet, consectetur adipiscing elit, sed do eiusmod tempor incididunt ut labore et dolore magna aliqua.</p><i class="glyph"></i></div>
  <div class="feat grp2" style="left:217px;top:1099px"><h4>Nurture</h4><p>Lorem ipsum dolor sit amet, consectetur adipiscing elit, sed do eiusmod tempor incididunt ut labore et dolore magna aliqua.</p><i class="glyph"></i></div>
  <div class="hub" style="left:175px;top:1007px;background:var(--a2)">Intent Data</div>

  <section class="sec services" style="top:1227px;height:195px">
    <div class="abs eyebrow center" style="top:18px">Our Services</div>
    <h2 class="abs outline center" style="top:34px">What We Do For Our Customers</h2>
    <div class="svc-card main" style="left:39px"><hr><h4>Marketing Qualified Leads <span style="float:right">→</span></h4><p>A Marketing Qualified Lead (MQL) is a prospect that has expressed an interest in what your brand has to offer. An MQL has taken the first steps to becoming a customer and is ready to receive additional contact from your company. Marketing Qualified Leads turn into Sales Qualified Leads once they have been through the buyer's journey.</p></div>
    <div class="svc-card photo" role="img" aria-label="Hands working on a smartphone beside printed charts" style="left:152px;background:linear-gradient(160deg,#d9c9b4,#b59a7c)"></div>
    <div class="svc-card photo" role="img" aria-label="Pen resting on a marketing strategy sketch next to a plant" style="left:265px;background:linear-gradient(160deg,#cfc6b8,#8f8576)"></div>
  </section>

  <section class="sec qa on-dark" style="top:1422px;height:181px">
    <div class="photo" role="img" aria-label="Glowing hand holding a rising data chart" style="left:170px;top:15px;width:238px;height:166px;background:radial-gradient(ellipse at 60% 45%,#3f8cff88 0%,#1632c000 65%)"></div>
    <div class="abs eyebrow" style="left:35px;top:19px">QA Technology</div>
    <h2 class="abs outline" style="left:35px;top:34px">Prospora &amp; Quality Assurance</h2>
    <div class="qa-item" style="top:70px"><i></i><div><b>Feedback</b><span>Tortor posuere ac ut consequat semper viverra nam</span></div></div>
    <div class="qa-item" style="top:93px"><i></i><div><b>Design</b><span>Tortor posuere ac ut consequat semper viverra nam</span></div></div>
    <div class="qa-item" style="top:116px"><i></i><div><b>Testing</b><span>Tortor posuere ac ut consequat semper viverra nam</span></div></div>
    <div class="qa-item" style="top:139px"><i></i><div><b>Development</b><span>Tortor posuere ac ut consequat semper viverra nam</span></div></div>
  </section>

  <section class="sec consult" style="top:1603px;height:79px">
    <h3 class="abs center" style="top:14px">Get a Consultancy</h3>
    <p class="abs center" style="top:31px">Lorem ipsum dolor sit amet, consectetur adipiscing elit, sed do eiusmod tempor incididunt ut labore et dolore magna aliqua.</p>
    <div class="field" style="left:39px">Name</div><div class="field" style="left:124px">E-Mail</div><div class="field" style="left:208px">Phone</div>
    <div class="pill">Consultancy <span>→</span></div>
  </section>

  <section class="sec testi" style="top:1682px;height:240px">
    <div class="abs eyebrow center" style="top:19px">Testimonials</div>
    <h2 class="abs outline center" style="top:35px">What do our Clients say</h2>
    <div class="stack" style="left:76px;top:170px;width:259px;height:18px"></div>
    <div class="stack" style="left:68px;top:168px;width:275px;height:14px"></div>
    <div class="quote-card" style="top:65px">
      <div class="avatar" role="img" aria-label="Client portrait"></div>
      <div class="who-name" style="top:72px">Rowan Pell</div>
      <div class="who-co" style="top:80px">Corvid, Inc.</div>
      <p class="quote">Lorem ipsum dolor sit amet, consectetur adipiscing elit, sed do eiusmod tempor incididunt ut labore et dolore magna aliqua. Ut enim ad minim veniam, quis nostrud exercitation ullamco laboris nisi ut aliquip ex ea commodo consequat. Duis aute irure dolor in reprehenderit in voluptate velit esse cillum dolore eu fugiat nulla pariatur. Excepteur sint occaecat cupidatat non proident, sunt in culpa qui officia deserunt mollit anim id est laborum.</p>
    </div>
    <div class="round" style="left:46px;top:113px">←</div><div class="round" style="left:340px;top:113px">→</div>
    <div class="more" style="top:201px">LEARN MORE <span>→</span></div>
  </section>

  <section class="sec intent on-dark" style="top:1922px;height:135px">
    <div class="photo" role="img" aria-label="Red glowing globe with network connections" style="left:0;top:0;width:210px;height:135px;background:radial-gradient(circle at 15% 65%,#e0212b 0%,#8b0a1055 45%,#00000000 70%)"></div>
    <div class="abs eyebrow" style="right:38px;top:19px;text-align:right">Intent Data</div>
    <h2 class="abs outline" style="right:38px;top:34px;text-align:right">How to Use Intent Data</h2>
    <p class="abs" style="right:38px;top:63px;width:220px">Our relationships with the world's most important technology &amp; business decision-makers generate a perpetual stream of global data. With access to 35 million individuals and a global behavioural data stream that is authenticated, timely and contextually relevant, we have one of the industry's most powerful signals of buyer intent and can fuel your demand-generation marketing strategies globally.</p>
    <p class="abs" style="right:38px;top:98px;width:220px">We support our intent targeting capabilities by partnering with a number of third party intent providers, meaning we are able to target the global data universe to deliver the best and most engaging leads to our partners.</p>
  </section>

  <section class="sec blog" style="top:2057px;height:273px">
    <div class="abs eyebrow center" style="top:19px">Blog</div>
    <h2 class="abs outline center" style="top:35px">Latest Blog Posts</h2>
    <span class="side-arrow" style="left:14px;top:136px">←</span><span class="side-arrow" style="left:390px;top:136px">→</span>
    <article class="post" style="left:45px"><div class="photo" role="img" aria-label="Laptop and printed reports on a desk" style="background:linear-gradient(160deg,#b9c6c9,#5f7a82)"></div><h4>What is QA Technology?</h4><p>Lorem ipsum dolor sit amet, consectetur adipiscing elit, sed do eiusmod tempor incididunt ut labore et dolore magna aliqua. Arcu cursus vitae congue.</p><div class="meta"><span>Milo Harker</span><span>3 days ago</span></div></article>
    <article class="post" style="left:157px"><div class="photo" role="img" aria-label="Hand holding a glowing blue chart" style="background:linear-gradient(160deg,#1b3fb8,#0a1550)"></div><h4>What is Intent Data?</h4><p>Lorem ipsum dolor sit amet, consectetur adipiscing elit, sed do eiusmod tempor incididunt ut labore et dolore magna aliqua. Arcu cursus vitae congue.</p><div class="meta"><span>Milo Harker</span><span>4 days ago</span></div></article>
    <article class="post" style="left:269px"><div class="photo" role="img" aria-label="Colleagues reviewing documents at a table" style="background:linear-gradient(160deg,#c5ccd6,#59647a)"></div><h4>What is QA Technology?</h4><p>Lorem ipsum dolor sit amet, consectetur adipiscing elit, sed do eiusmod tempor incididunt ut labore et dolore magna aliqua. Arcu cursus vitae congue.</p><div class="meta"><span>Milo Harker</span><span>6 days ago</span></div></article>
    <div class="more" style="top:234px">LEARN MORE <span>→</span></div>
  </section>

  <footer class="sec footer">
    <div class="fcol" style="left:17px"><h5>Company</h5><ul><li>About</li><li>Team</li><li>News</li><li>Career</li><li>Contact Us</li></ul></div>
    <div class="fcol" style="left:82px"><h5>Solutions</h5><ul><li>Marketing Qualified Leads</li><li>Account Based Marketing Leads</li><li>Sales Qualified Lead</li><li>QA Technology</li><li>Intent Data</li></ul></div>
    <div class="fcol" style="left:180px"><h5>Support</h5><ul><li>Blog</li><li>Knowledge Base</li><li>Privacy Policy</li><li>Terms and Conditions</li></ul></div>
    <div class="fcol" style="left:278px;width:115px"><h5>Newsletter</h5><ul><li style="line-height:5px">Subscribe to our newsletter to receive weekly news, updates, special offers and exclusive extra discounts.</li></ul></div>
    <div class="news-field">E-Mail <span style="float:right">➤</span></div>
  </footer>
  <div class="sec base">
    <div class="photo" role="img" aria-label="Dark street map of London" style="left:246px;top:0;width:162px;height:121px;background:linear-gradient(150deg,#3a3a3d,#1c1c1e)"></div>
    <div class="abs brand" style="left:14px;top:22px;font-size:9px"><i style="width:13px;height:13px"></i><div>ledgerwisereach<small>The Demand Generation Company</small></div></div>
    <p class="abs" style="left:14px;top:50px;width:120px">Lorem ipsum dolor sit amet, consectetur adipiscing elit, sed do eiusmod tempor incididunt ut labore et dolore magna aliqua. Arcu cursus vitae congue mauris rhoncus aenean vel elit scelerisque.</p>
    <div class="abs" style="left:14px;top:86px;font-size:4px">Connect with us <span class="dot" style="margin-left:9px"></span><span class="dot"></span><span class="dot"></span><span class="dot"></span></div>
    <p class="abs" style="left:14px;top:106px;font-size:2.8px">Ledgerwise Reach © All rights reserved</p>
  </div>
  <div class="reach-box" style="top:2433px;height:72px;background:var(--a1)"><span>Our team are standing by to help you find the right solution</span><b>+44 20 7946 0321</b></div>
  <div class="reach-box" style="top:2505px;height:71px;background:var(--a1d);padding-top:18px"><span>Our team are standing by to help you find the right solution</span><b>hi@ledgerwisereach.example</b></div>
</div>

<!-- ============ Red theme ============ -->
<div class="site theme-red" style="left:744px">

  <section class="sec hero">
    <div class="photo" role="img" aria-label="Portrait of a businessman in a suit adjusting his tie" style="left:225px;top:0;width:183px;height:198px;background:linear-gradient(180deg,#2a1a1c 0%,#4a2e2a 50%,#160c0e 100%)"></div>
    <div class="abs brand" style="left:38px;top:10px"><i></i><div>ledgerwisereach<small>The Demand Generation Company</small></div></div>
    <nav class="abs nav" style="left:162px;top:15px"><span>Home</span><span>About</span><span>Services</span><span>Prospora &amp; QA Technology</span><span>Intent Data</span><span>Testimonials</span><span>Contact</span></nav>
    <h1 class="abs" style="left:40px;top:62px">Grow Your Business With<br>Ledgerwise Reach</h1>
    <p class="abs" style="left:40px;top:110px">Check out our marketing, sales and services to that helps your business grow. Getting good service will ensure that your customers receive good service.</p>
    <div class="abs play" style="left:41px;top:141px"><svg width="4" height="5" viewBox="0 0 4 5"><path d="M0 0L4 2.5L0 5Z" fill="#fff"/></svg></div>
    <div class="abs pill" style="left:62px;top:141px;width:47px;height:12px;background:var(--a1)">GET STARTED <span>→</span></div>
  </section>

  <div class="abs phone-box" style="padding:9px 15px">
    <b>&#9990; +44 20 7946 0321</b><br><span>Monday - Friday 9:00AM - 6:00PM</span>
    <span class="abs arrow" style="left:112px;top:11px">‹</span><span class="abs arrow" style="left:139px;top:11px">›</span>
  </div>
  <div class="sec clients">
    <div class="client" style="left:10px"><i></i>Brindlow</div>
    <div class="client" style="left:64px">Norvex</div>
    <div class="client" style="left:112px">QRT</div>
    <div class="client" style="left:160px">Tarvo</div>
    <div class="client" style="left:208px">VKD</div>
  </div>
  <div class="abs who">WHO WE WORK WITH</div>
  <div class="abs consult-tab">
    <span class="abs arrow" style="left:11px;top:11px">‹</span><span class="abs arrow" style="left:38px;top:11px">›</span>
    <div class="abs" style="left:70px;top:7px;width:78px"><b>&#9993; Free Consultation</b><span>Request a free assessment and get started today.</span></div>
  </div>

  <div class="abs eyebrow center" style="top:284px">About Us</div>
  <h2 class="abs outline center" style="top:300px">Marketing and Advertising Solutions<br>for Your Business</h2>
  <div class="abs body-copy" style="left:39px;top:357px;width:160px">
    <p>Ledgerwise Reach can deliver high quality sales leads from any country in the world. This can include leads via email or telemarketing, account-based targeting (ABM) or identifying need and pain points through BANT / SQL campaigns.</p>
    <p>Ledgerwise Reach offer expert demand generation support, from providing detailed leads of qualified decision makers, to a comprehensive lead generation and SQL service.</p>
    <p>Our extensive and ongoing research campaigns give you the ability to build contact lists that identify individuals at all stages of the buying cycle, from pre-sales to sales ready.</p>
    <p>With access to over 31 million names, Ledgerwise Reach offers a range of marketing options that allow you to use our data to target the decision makers you need to reach.</p>
    <p>This can include:</p>
    <ul class="ticks">
      <li><svg viewBox="0 0 8 8"><circle cx="4" cy="4" r="4" fill="var(--tick)"/><path d="M2.2 4.1L3.5 5.3L5.9 2.8" stroke="#fff" stroke-width=".9" fill="none"/></svg>Breakdown by geography, job title, role and responsibility</li>
      <li><svg viewBox="0 0 8 8"><circle cx="4" cy="4" r="4" fill="var(--tick)"/><path d="M2.2 4.1L3.5 5.3L5.9 2.8" stroke="#fff" stroke-width=".9" fill="none"/></svg>Targeting through previous research and buying intention</li>
      <li><svg viewBox="0 0 8 8"><circle cx="4" cy="4" r="4" fill="var(--tick)"/><path d="M2.2 4.1L3.5 5.3L5.9 2.8" stroke="#fff" stroke-width=".9" fill="none"/></svg>Email dispatch to selected individuals</li>
      <li><svg viewBox="0 0 8 8"><circle cx="4" cy="4" r="4" fill="var(--tick)"/><path d="M2.2 4.1L3.5 5.3L5.9 2.8" stroke="#fff" stroke-width=".9" fill="none"/></svg>Extensive telemarketing options</li>
    </ul>
  </div>
  <div class="photo" role="img" aria-label="Glass office towers seen from below against a blue sky" style="left:208px;top:357px;width:161px;height:185px;background:linear-gradient(160deg,#dfe9f3 0%,#8fb0cc 40%,#3b6b93 100%)"></div>
  <div class="photo" role="img" aria-label="Team meeting in a bright glass-walled office" style="left:201px;top:447px;width:78px;height:102px;border:4px solid #fff;background:linear-gradient(170deg,#c9d3da,#6f7f8a)"></div>

  <div class="stat lead" style="left:149px;top:587px;width:109px;height:52px"><span>Leads Delivered Per Month</span><b>25.000+</b></div>
  <div class="stat" style="left:39px;top:640px;width:109px;height:53px"><span>Downloads Per Month</span><b>70.000+</b></div>
  <div class="stat" style="left:259px;top:640px;width:109px;height:53px"><span>Countries We Can Reach</span><b>50+</b></div>

  <div class="abs rail" style="top:680px;height:497px;background:linear-gradient(180deg,var(--a1) 0%,var(--a1) 52%,var(--a2) 52%,var(--a2) 100%);opacity:.5"></div>
  <div class="node" style="left:201.5px;top:678px;background:var(--a1)"></div>
  <div class="node" style="left:201.5px;top:1175px;background:var(--a2)"></div>

  <div class="feat grp1 on1" style="left:71px;top:727px"><h4>Service</h4><p>Lorem ipsum dolor sit amet, consectetur adipiscing elit, sed do eiusmod tempor incididunt ut labore et dolore magna aliqua.</p><i class="glyph"></i></div>
  <div class="feat grp1" style="left:217px;top:727px"><h4>Improvement</h4><p>Lorem ipsum dolor sit amet, consectetur adipiscing elit, sed do eiusmod tempor incididunt ut labore et dolore magna aliqua.</p><i class="glyph"></i></div>
  <div class="feat grp1" style="left:39px;top:812px"><h4>Satisfaction</h4><p>Lorem ipsum dolor sit amet, consectetur adipiscing elit, sed do eiusmod tempor incididunt ut labore et dolore magna aliqua.</p><i class="glyph"></i></div>
  <div class="feat grp1" style="left:248px;top:812px"><h4>Business</h4><p>Lorem ipsum dolor sit amet, consectetur adipiscing elit, sed do eiusmod tempor incididunt ut labore et dolore magna aliqua.</p><i class="glyph"></i></div>
  <div class="feat grp1" style="left:71px;top:896px"><h4>Standard</h4><p>Lorem ipsum dolor sit amet, consectetur adipiscing elit, sed do eiusmod tempor incididunt ut labore et dolore magna aliqua.</p><i class="glyph"></i></div>
  <div class="feat grp1" style="left:217px;top:896px"><h4>Customer</h4><p>Lorem ipsum dolor sit amet, consectetur adipiscing elit, sed do eiusmod tempor incididunt ut labore et dolore magna aliqua.</p><i class="glyph"></i></div>
  <div class="hub" style="left:175px;top:816px;background:var(--a1)">QA Technology</div>

  <div class="feat grp2 on2" style="left:39px;top:1015px"><h4>Generate</h4><p>Lorem ipsum dolor sit amet, consectetur adipiscing elit, sed do eiusmod tempor incididunt ut labore et dolore magna aliqua.</p><i class="glyph"></i></div>
  <div class="feat grp2" style="left:248px;top:1015px"><h4>Capture</h4><p>Lorem ipsum dolor sit amet, consectetur adipiscing elit, sed do eiusmod tempor incididunt ut labore et dolore magna aliqua.</p><i class="glyph"></i></div>
  <div class="feat grp2" style="left:71px;top:1099px"><h4>Qualify</h4><p>Lorem ipsum dolor sit amet, consectetur adipiscing elit, sed do eiusmod tempor incididunt ut labore et dolore magna aliqua.</p><i class="glyph"></i></div>
  <div class="feat grp2" style="left:217px;top:1099px"><h4>Nurture</h4><p>Lorem ipsum dolor sit amet, consectetur adipiscing elit, sed do eiusmod tempor incididunt ut labore et dolore magna aliqua.</p><i class="glyph"></i></div>
  <div class="hub" style="left:175px;top:1007px;background:var(--a2)">Intent Data</div>

  <section class="sec services" style="top:1227px;height:195px">
    <div class="abs eyebrow center" style="top:18px">Our Services</div>
    <h2 class="abs outline center" style="top:34px">What We Do For Our Customers</h2>
    <div class="svc-card main" style="left:39px"><hr><h4>Marketing Qualified Leads <span style="float:right">→</span></h4><p>A Marketing Qualified Lead (MQL) is a prospect that has expressed an interest in what your brand has to offer. An MQL has taken the first steps to becoming a customer and is ready to receive additional contact from your company. Marketing Qualified Leads turn into Sales Qualified Leads once they have been through the buyer's journey.</p></div>
    <div class="svc-card photo" role="img" aria-label="Hands working on a smartphone beside printed charts" style="left:152px;background:linear-gradient(160deg,#d9c9b4,#b59a7c)"></div>
    <div class="svc-card photo" role="img" aria-label="Pen resting on a marketing strategy sketch next to a plant" style="left:265px;background:linear-gradient(160deg,#cfc6b8,#8f8576)"></div>
  </section>

  <section class="sec qa on-dark" style="top:1422px;height:181px">
    <div class="photo" role="img" aria-label="Glowing hand holding a rising data chart" style="left:170px;top:15px;width:238px;height:166px;background:radial-gradient(ellipse at 60% 45%,#3f8cff88 0%,#1632c000 65%)"></div>
    <div class="abs eyebrow" style="left:35px;top:19px">QA Technology</div>
    <h2 class="abs outline" style="left:35px;top:34px">Prospora &amp; Quality Assurance</h2>
    <div class="qa-item" style="top:70px"><i style="background:var(--a1)"></i><div><b>Feedback</b><span>Tortor posuere ac ut consequat semper viverra nam</span></div></div>
    <div class="qa-item" style="top:93px"><i style="background:var(--a1)"></i><div><b>Design</b><span>Tortor posuere ac ut consequat semper viverra nam</span></div></div>
    <div class="qa-item" style="top:116px"><i style="background:var(--a1)"></i><div><b>Testing</b><span>Tortor posuere ac ut consequat semper viverra nam</span></div></div>
    <div class="qa-item" style="top:139px"><i style="background:var(--a1)"></i><div><b>Development</b><span>Tortor posuere ac ut consequat semper viverra nam</span></div></div>
  </section>

  <section class="sec testi" style="top:1603px;height:240px">
    <div class="abs eyebrow center" style="top:20px">Testimonials</div>
    <h2 class="abs outline center" style="top:36px">What do our Clients say</h2>
    <div class="stack" style="left:76px;top:172px;width:259px;height:18px"></div>
    <div class="stack" style="left:68px;top:170px;width:275px;height:14px"></div>
    <div class="quote-card" style="top:65px">
      <div class="avatar" role="img" aria-label="Client portrait"></div>
      <div class="who-name" style="top:72px">Rowan Pell</div>
      <div class="who-co" style="top:80px">Corvid, Inc.</div>
      <p class="quote">Lorem ipsum dolor sit amet, consectetur adipiscing elit, sed do eiusmod tempor incididunt ut labore et dolore magna aliqua. Ut enim ad minim veniam, quis nostrud exercitation ullamco laboris nisi ut aliquip ex ea commodo consequat. Duis aute irure dolor in reprehenderit in voluptate velit esse cillum dolore eu fugiat nulla pariatur. Excepteur sint occaecat cupidatat non proident, sunt in culpa qui officia deserunt mollit anim id est laborum.</p>
    </div>
    <div class="round" style="left:46px;top:113px">←</div><div class="round" style="left:340px;top:113px">→</div>
    <div class="more" style="top:200px">LEARN MORE <span>→</span></div>
  </section>

  <section class="sec intent on-dark" style="top:1843px;height:135px">
    <div class="photo" role="img" aria-label="Red glowing globe with network connections" style="left:0;top:0;width:210px;height:135px;background:radial-gradient(circle at 15% 65%,#e0212b 0%,#8b0a1055 45%,#00000000 70%)"></div>
    <div class="abs eyebrow" style="right:38px;top:19px;text-align:right">Intent Data</div>
    <h2 class="abs outline" style="right:38px;top:34px;text-align:right">How to Use Intent Data</h2>
    <p class="abs" style="right:38px;top:63px;width:220px">Our relationships with the world's most important technology &amp; business decision-makers generate a perpetual stream of global data. With access to 35 million individuals and a global behavioural data stream that is authenticated, timely and contextually relevant, we have one of the industry's most powerful signals of buyer intent and can fuel your demand-generation marketing strategies globally.</p>
    <p class="abs" style="right:38px;top:98px;width:220px">We support our intent targeting capabilities by partnering with a number of third party intent providers, meaning we are able to target the global data universe to deliver the best and most engaging leads to our partners.</p>
  </section>

  <section class="sec consult" style="top:1978px;height:79px;background:linear-gradient(180deg,#d81e33,var(--a1))">
    <h3 class="abs center" style="top:14px">Get a Consultancy</h3>
    <p class="abs center" style="top:31px">Lorem ipsum dolor sit amet, consectetur adipiscing elit, sed do eiusmod tempor incididunt ut labore et dolore magna aliqua.</p>
    <div class="field" style="left:39px">Name</div><div class="field" style="left:124px">E-Mail</div><div class="field" style="left:208px">Phone</div>
    <div class="pill">Consultancy <span>→</span></div>
  </section>

  <section class="sec blog" style="top:2057px;height:273px">
    <div class="abs eyebrow center" style="top:19px">Blog</div>
    <h2 class="abs outline center" style="top:35px">Latest Blog Posts</h2>
    <span class="side-arrow" style="left:14px;top:136px">←</span><span class="side-arrow" style="left:390px;top:136px">→</span>
    <article class="post" style="left:45px"><div class="photo" role="img" aria-label="Laptop and printed reports on a desk" style="background:linear-gradient(160deg,#b9c6c9,#5f7a82)"></div><h4>What is QA Technology?</h4><p>Lorem ipsum dolor sit amet, consectetur adipiscing elit, sed do eiusmod tempor incididunt ut labore et dolore magna aliqua. Arcu cursus vitae congue.</p><div class="meta"><span>Milo Harker</span><span>3 days ago</span></div></article>
    <article class="post" style="left:157px"><div class="photo" role="img" aria-label="Hand holding a glowing blue chart" style="background:linear-gradient(160deg,#1b3fb8,#0a1550)"></div><h4>What is Intent Data?</h4><p>Lorem ipsum dolor sit amet, consectetur adipiscing elit, sed do eiusmod tempor incididunt ut labore et dolore magna aliqua. Arcu cursus vitae congue.</p><div class="meta"><span>Milo Harker</span><span>4 days ago</span></div></article>
    <article class="post" style="left:269px"><div class="photo" role="img" aria-label="Colleagues reviewing documents at a table" style="background:linear-gradient(160deg,#c5ccd6,#59647a)"></div><h4>What is QA Technology?</h4><p>Lorem ipsum dolor sit amet, consectetur adipiscing elit, sed do eiusmod tempor incididunt ut labore et dolore magna aliqua. Arcu cursus vitae congue.</p><div class="meta"><span>Milo Harker</span><span>6 days ago</span></div></article>
    <div class="more" style="top:234px">LEARN MORE <span>→</span></div>
  </section>

  <footer class="sec footer">
    <div class="fcol" style="left:17px"><h5>Company</h5><ul><li>About</li><li>Team</li><li>News</li><li>Career</li><li>Contact Us</li></ul></div>
    <div class="fcol" style="left:82px"><h5>Solutions</h5><ul><li>Marketing Qualified Leads</li><li>Account Based Marketing Leads</li><li>Sales Qualified Lead</li><li>QA Technology</li><li>Intent Data</li></ul></div>
    <div class="fcol" style="left:180px"><h5>Support</h5><ul><li>Blog</li><li>Knowledge Base</li><li>Privacy Policy</li><li>Terms and Conditions</li></ul></div>
    <div class="fcol" style="left:278px;width:115px"><h5>Newsletter</h5><ul><li style="line-height:5px">Subscribe to our newsletter to receive weekly news, updates, special offers and exclusive extra discounts.</li></ul></div>
    <div class="news-field">E-Mail <span style="float:right">➤</span></div>
  </footer>
  <div class="sec base">
    <div class="photo" role="img" aria-label="Dark street map of London" style="left:246px;top:0;width:162px;height:121px;background:linear-gradient(150deg,#3a3a3d,#1c1c1e)"></div>
    <div class="abs brand" style="left:14px;top:22px;font-size:9px"><i style="width:13px;height:13px"></i><div>ledgerwisereach<small>The Demand Generation Company</small></div></div>
    <p class="abs" style="left:14px;top:50px;width:120px">Lorem ipsum dolor sit amet, consectetur adipiscing elit, sed do eiusmod tempor incididunt ut labore et dolore magna aliqua. Arcu cursus vitae congue mauris rhoncus aenean vel elit scelerisque.</p>
    <div class="abs" style="left:14px;top:86px;font-size:4px">Connect with us <span class="dot" style="margin-left:9px"></span><span class="dot"></span><span class="dot"></span><span class="dot"></span></div>
    <p class="abs" style="left:14px;top:106px;font-size:2.8px">Ledgerwise Reach © All rights reserved</p>
  </div>
  <div class="reach-box" style="top:2433px;height:72px;background:var(--a1)"><span>Our team are standing by to help you find the right solution</span><b>+44 20 7946 0321</b></div>
  <div class="reach-box" style="top:2505px;height:71px;background:var(--a1d);padding-top:18px"><span>Our team are standing by to help you find the right solution</span><b>hi@ledgerwisereach.example</b></div>
</div>

</div>
</body>
</html>
```